A Freight forwarding (transportation/shipping) company requires stationary designs

We need The following:
1. Letterhead
2. Letter Envelope
3. Business Card Design
4. A4 Paper Envelope
5. A4 Paper Folder (One that is 2xA4 foldable size which we can open in half and we can put a paper in between and has a lot for business card)
6. A5 Paper (To be used for notes taking)
a design for a freight forwarding company named KORVALE DIMAS INTERNATIONAL TRANSPORTATION.
(We are active in Sea Transportation, Truck transportation, and Air Transportation, (printed design in PDF is required with all open source files for editing - lamination accepted)
Playing around with the Logo is accepted,, Korvale Logo.png is the correct logo.
Example of folder, envelopes, and notepad attached
Address of the company is :
No 7, 4th Tarvandi Gharbi, Nasim Dareh Blvd,
Mashhad, IR
Tel : +98 51 30000000
Fax : +98 51 30000001
Website : www.korvale-example.com
Email : info@korvale-example.com

```html
<!DOCTYPE html>
<html lang="en">
<head>
<meta charset="utf-8">
<title>Korvale Dimas Stationery Set</title>
<link href="https://fonts.googleapis.com/css2?family=Open+Sans:wght@400;600;700&display=swap" rel="stylesheet">
<style>
:root{
  --bg:#c3c3c3;
  --paper:#ffffff;
  --brand-blue:#3c3c96;
  --brand-green:#3b9a3b;
  --ink:#222233;
  --rule:#b9b9c4;
  --shadow:rgba(0,0,0,.18);
}
*{box-sizing:border-box;margin:0;padding:0}
html,body{width:1200px;height:969px;overflow:hidden}
body{background:var(--bg);font-family:"Open Sans",Arial,sans-serif;color:var(--ink);position:relative}
.sheet{position:absolute;background:var(--paper);box-shadow:0 1px 3px var(--shadow);overflow:hidden}
.wave{position:absolute;left:0;bottom:0;width:100%;display:block}
.env-flap{position:absolute;left:0;top:0;width:100%;display:block}
.brand{display:flex;flex-direction:column;align-items:center;text-align:center}
.brand-row{display:flex;align-items:center;gap:4px}
.brand-dot{border-radius:50%;background:var(--brand-blue)}
.brand-name{color:var(--brand-blue);font-weight:700;white-space:nowrap}
.brand-sub{color:var(--ink);white-space:nowrap}
.contact{border-left:1px solid var(--brand-blue);color:var(--ink);line-height:1.3}
.contact .line{display:flex;align-items:center;gap:4px;white-space:nowrap}
.ico{display:inline-block;border-radius:50%;background:var(--brand-blue);flex:none}
.letter-body{position:absolute;font-size:4.6px;line-height:1.55;text-align:justify}
.letter-body p{margin-bottom:5px}
.ruled{position:absolute;left:18px;right:14px}
.ruled i{display:block;height:1px;background:var(--rule);margin-bottom:9.6px}
</style>
</head>
<body>

<!-- Envelope back, top left -->
<div class="sheet" style="left:36px;top:40px;width:246px;height:350px">
  <svg class="env-flap" viewBox="0 0 246 60" height="60"><path d="M0 0 L0 12 Q120 75 246 12 L246 0" fill="none" stroke="#d8d8d8" stroke-width="1"/></svg>
</div>

<!-- Letterhead, top left -->
<div class="sheet letterhead-small" style="left:120px;top:100px;width:248px;height:350px">
  <div style="position:absolute;left:12px;top:16px;display:flex;gap:6px">
    <div class="brand" style="width:36px">
      <div class="brand-row"><span class="brand-dot" style="width:5px;height:5px"></span><span class="brand-name" style="font-size:4px">KORVALE DIMAS</span></div>
      <span class="brand-sub" style="font-size:2.5px">International Transportation</span>
    </div>
    <div class="contact" style="font-size:2.6px;padding-left:5px">
      <div>No 7, 4th Tarvandi Gharbi,<br>Nasim Dareh Blvd, Mashhad, IR</div>
      <div class="line">+98 51 30000000</div>
      <div class="line">+98 51 30000001</div>
      <div class="line">info@korvale-example.com</div>
      <div class="line">www.korvale-example.com</div>
    </div>
  </div>
  <svg class="wave" viewBox="0 0 248 24" height="24" preserveAspectRatio="none"><path d="M0 24 C90 4 190 -2 248 12 L248 24Z" fill="var(--brand-green)"/><path d="M0 24 C90 8 190 2 248 16 L248 24Z" fill="var(--brand-blue)"/></svg>
</div>

<!-- Folder -->
<svg style="position:absolute;left:460px;top:30px" width="592" height="446" viewBox="0 0 592 446" class="folder">
  <path d="M0 31 L52 0 L52 381 L0 349Z" fill="#44449a"/>
  <rect x="52" y="0" width="270" height="381" fill="var(--brand-blue)"/>
  <path d="M52 381 L322 381 L277 445 L52 445Z" fill="#45459b"/>
  <rect x="322" y="0" width="269" height="381" fill="var(--paper)"/>
</svg>
<div style="position:absolute;left:530px;top:358px;display:flex;gap:6px;color:#fff" class="folder-contact">
  <div class="brand" style="width:38px">
    <div class="brand-row"><span class="brand-dot" style="width:5px;height:5px;background:#fff"></span><span class="brand-name" style="font-size:4px;color:#fff">KORVALE DIMAS</span></div>
    <span class="brand-sub" style="font-size:2.5px;color:#fff">International Transportation</span>
  </div>
  <div class="contact" style="font-size:3.4px;padding-left:6px;border-color:#fff;color:#fff">
    <div>No 7, 4th Tarvandi Gharbi,<br>Nasim Dareh Blvd, Mashhad, IR</div>
    <div style="margin-top:3px">+98 51 30000000</div>
    <div>+98 51 30000001</div>
    <div>info@korvale-example.com</div>
    <div>www.korvale-example.com</div>
  </div>
</div>
<div class="brand" style="position:absolute;left:846px;top:330px;width:120px">
  <div class="brand-row"><span class="brand-dot" style="width:12px;height:12px"></span><span class="brand-name" style="font-size:10px">KORVALE DIMAS</span></div>
  <span class="brand-sub" style="font-size:5px;margin-top:2px">International Transportation</span>
</div>

<!-- Envelope back, bottom left -->
<div class="sheet" style="left:26px;top:486px;width:274px;height:354px">
  <svg class="env-flap" viewBox="0 0 274 64" height="64"><path d="M0 0 L0 12 Q135 80 274 12 L274 0" fill="none" stroke="#d8d8d8" stroke-width="1"/></svg>
</div>

<!-- Letterhead with content -->
<div class="sheet letterhead" style="left:74px;top:546px;width:274px;height:353px">
  <div class="brand" style="position:absolute;left:18px;top:24px;width:60px">
    <div class="brand-row"><span class="brand-dot" style="width:6px;height:6px"></span><span class="brand-name" style="font-size:5.5px">KORVALE DIMAS</span></div>
    <span class="brand-sub" style="font-size:3px">International Transportation</span>
  </div>
  <div class="contact" style="position:absolute;left:180px;top:20px;font-size:4px;padding-left:7px">
    <div>No 7, 4th Tarvandi Gharbi,<br>Nasim Dareh Blvd, Mashhad, IR</div>
    <div class="line" style="margin-top:3px"><span class="ico" style="width:3px;height:3px"></span>+98 51 30000000</div>
    <div class="line"><span class="ico" style="width:3px;height:3px"></span>+98 51 30000001</div>
    <div class="line"><span class="ico" style="width:3px;height:3px"></span>info@korvale-example.com</div>
    <div class="line"><span class="ico" style="width:3px;height:3px"></span>www.korvale-example.com</div>
  </div>
  <div class="letter-body" style="left:28px;top:86px;width:220px">
    <p>LOREM IPSUM DOLOR<br>sit amet consectetur elit.<br>Nunc vitae purus magna<br>Morbi tempus nisi ac<br>tincidunt, ut arcu,</p>
    <p>Lorem ipsum dolor sit amet, consectetuer adipiscing elit. Aenean commodo ligula eget dolor. Aenean massa. Cum sociis natoque penatibus et magnis dis parturient montes, nascetur ridiculus mus. Donec quam felis, ultricies nec, pellentesque eu, pretium quis, sem. Nulla consequat massa quis enim. Donec pede justo, fringilla vel, aliquet nec, vulputate eget, arcu. In enim justo, rhoncus ut, imperdiet a, venenatis vitae, justo. Nullam dictum felis eu pede mollis pretium. Integer tincidunt. Cras dapibus. Vivamus elementum semper nisi. Aenean vulputate eleifend tellus. Aenean leo ligula, porttitor eu, consequat vitae, eleifend ac, enim. Aliquam lorem ante, dapibus in, viverra quis, feugiat a, tellus.</p>
    <p>Phasellus viverra nulla ut metus varius laoreet. Quisque rutrum. Aenean imperdiet. Etiam ultricies nisi vel augue. Curabitur ullamcorper ultricies nisi. Nam eget dui. Etiam rhoncus. Maecenas tempus, tellus eget condimentum rhoncus, sem quam semper libero, sit amet adipiscing sem neque sed ipsum. Nam quam nunc, blandit vel, luctus pulvinar, hendrerit id, lorem. Maecenas nec odio et ante tincidunt tempus. Donec vitae sapien ut libero venenatis faucibus. Nullam quis ante.</p>
    <p>Vestibulum purus quam, scelerisque ut, mollis sed, nonummy id, metus. Nullam accumsan lorem in dui. Cras ultricies mi eu turpis hendrerit fringilla. Vestibulum ante ipsum primis in faucibus orci luctus et ultrices posuere cubilia Curae; In ac dui quis mi consectetuer lacinia.</p>
    <p style="text-align:right;font-weight:600">Signed name</p>
  </div>
  <div role="img" aria-label="Handwritten signature" style="position:absolute;left:214px;top:300px;width:40px;height:22px;background:#ececf2"></div>
  <svg class="wave" viewBox="0 0 274 26" height="26" preserveAspectRatio="none"><path d="M0 26 C100 4 210 -2 274 12 L274 26Z" fill="var(--brand-green)"/><path d="M0 26 C100 8 210 2 274 16 L274 26Z" fill="var(--brand-blue)"/></svg>
</div>

<!-- DL envelope front -->
<svg style="position:absolute;left:441px;top:498px" width="346" height="78" viewBox="0 0 346 78" class="dl-flap">
  <path d="M0 76 C0 40 100 20 172 0 C250 20 346 40 346 76Z" fill="var(--paper)"/>
</svg>
<div class="sheet dl-envelope" style="left:441px;top:574px;width:346px;height:148px;overflow:visible;box-shadow:none">
  <div class="brand" style="position:absolute;left:130px;top:-50px;width:86px">
    <div class="brand-row"><span class="brand-dot" style="width:6px;height:6px"></span><span class="brand-name" style="font-size:5.5px">KORVALE DIMAS</span></div>
    <span class="brand-sub" style="font-size:3px">International Transportation</span>
  </div>
  <div class="brand" style="position:absolute;left:10px;top:24px;width:56px">
    <div class="brand-row"><span class="brand-dot" style="width:6px;height:6px"></span><span class="brand-name" style="font-size:5.2px">KORVALE DIMAS</span></div>
    <span class="brand-sub" style="font-size:3px">International Transportation</span>
  </div>
  <div class="contact" style="position:absolute;left:64px;top:12px;font-size:4.2px;padding-left:7px">
    <div>No 7, 4th Tarvandi Gharbi,<br>Nasim Dareh Blvd, Mashhad, IR</div>
    <div class="line" style="margin-top:3px"><span class="ico" style="width:3px;height:3px"></span>+98 51 30000000</div>
    <div class="line"><span class="ico" style="width:3px;height:3px"></span>+98 51 30000001</div>
    <div class="line"><span class="ico" style="width:3px;height:3px"></span>info@korvale-example.com</div>
    <div class="line"><span class="ico" style="width:3px;height:3px"></span>www.korvale-example.com</div>
  </div>
  <svg class="wave" viewBox="0 0 346 32" height="32" preserveAspectRatio="none"><path d="M0 32 C110 8 250 -2 346 14 L346 32Z" fill="var(--brand-green)"/><path d="M0 32 C110 12 250 3 346 19 L346 32Z" fill="var(--brand-blue)"/></svg>
</div>

<!-- Business card front -->
<div class="sheet card-front" style="left:389px;top:760px;width:226px;height:128px">
  <div class="brand" style="position:absolute;left:14px;top:48px;width:80px">
    <div class="brand-row"><span class="brand-dot" style="width:8px;height:8px"></span><span class="brand-name" style="font-size:7px">KORVALE DIMAS</span></div>
    <span class="brand-sub" style="font-size:3.6px;margin-top:1px">International Transportation</span>
  </div>
  <div class="contact" style="position:absolute;left:109px;top:20px;height:76px;font-size:6.2px;padding-left:10px;line-height:1.25">
    <div style="color:var(--brand-blue);font-weight:700;font-size:7px">Your Name Here</div>
    <div>Managing Director</div>
    <div style="margin-top:6px">No 7, 4th Tarvandi Gharbi,<br>Nasim Dareh Blvd, Mashhad, IR</div>
    <div class="line" style="margin-top:5px"><span class="ico" style="width:4px;height:4px"></span>+98 51 30000000</div>
    <div class="line"><span class="ico" style="width:4px;height:4px"></span>+98 51 30000001</div>
    <div class="line"><span class="ico" style="width:4px;height:4px"></span>info@korvale-example.com</div>
    <div class="line"><span class="ico" style="width:4px;height:4px"></span>www.korvale-example.com</div>
  </div>
  <svg class="wave" viewBox="0 0 226 22" height="22" preserveAspectRatio="none"><path d="M0 22 C80 4 170 -2 226 12 L226 22Z" fill="var(--brand-green)"/><path d="M0 22 C80 8 170 2 226 16 L226 22Z" fill="var(--brand-blue)"/></svg>
</div>

<!-- Business card back -->
<div class="sheet card-back" style="left:630px;top:760px;width:229px;height:130px;background:var(--brand-blue)">
  <div class="brand" style="position:absolute;left:40px;top:52px;width:149px">
    <div class="brand-row"><span class="brand-dot" style="width:10px;height:10px;background:#fff"></span><span class="brand-name" style="font-size:10px;color:#fff">KORVALE DIMAS</span></div>
    <span class="brand-sub" style="font-size:5px;color:#fff;margin-top:2px">International Transportation</span>
  </div>
</div>

<!-- Notepad, back sheet -->
<div class="sheet notepad" style="left:914px;top:566px;width:227px;height:322px">
  <div class="ruled" style="top:64px;left:20px">
    <i></i><i></i><i></i><i></i><i></i><i></i><i></i><i></i><i></i><i></i><i></i><i></i><i></i><i></i><i></i><i></i><i></i><i></i><i></i><i></i><i></i><i></i><i></i><i></i>
  </div>
  <svg class="wave" viewBox="0 0 227 22" height="22" preserveAspectRatio="none"><path d="M0 22 C80 4 170 -2 227 12 L227 22Z" fill="var(--brand-green)"/><path d="M0 22 C80 8 170 2 227 16 L227 22Z" fill="var(--brand-blue)"/></svg>
</div>

<!-- Notepad, front sheet -->
<div class="sheet notepad" style="left:878px;top:503px;width:227px;height:321px">
  <div class="brand" style="position:absolute;left:12px;top:16px;width:50px">
    <div class="brand-row"><span class="brand-dot" style="width:5px;height:5px"></span><span class="brand-name" style="font-size:4.2px">KORVALE DIMAS</span></div>
    <span class="brand-sub" style="font-size:2.5px">International Transportation</span>
  </div>
  <div class="ruled" style="top:62px">
    <i></i><i></i><i></i><i></i><i></i><i></i><i></i><i></i><i></i><i></i><i></i><i></i><i></i><i></i><i></i><i></i><i></i><i></i><i></i><i></i><i></i><i></i><i></i><i></i><i></i><i></i>
  </div>
  <svg class="wave" viewBox="0 0 227 22" height="22" preserveAspectRatio="none"><path d="M0 22 C80 4 170 -2 227 12 L227 22Z" fill="var(--brand-green)"/><path d="M0 22 C80 8 170 2 227 16 L227 22Z" fill="var(--brand-blue)"/></svg>
</div>

</body>
</html>
```